WE WOULD LIKE TO HAVE PROFESSIONAL LOOK ALLERGEN MATRIX DESIGN.
Our company is KESTRAN WORKS LIMITED.
I am sharing a competitors design as well.
We would like to have grafics for 14 allergens. At the end of the allergen matrix we would like to have a like a list for review details and approval date. I am also attaching an example what we are using right now.
We would like to signs for may contain, contains, removable, additionally GMO and Colorant

```html
<!DOCTYPE html>
<html lang="en">
<head>
<meta charset="utf-8">
<title>Allergen Matrix – Kestran Works Limited</title>
<link href="https://fonts.googleapis.com/css2?family=Montserrat:wght@400;600;700;800&family=Open+Sans:wght@400;600;700&display=swap" rel="stylesheet">
<style>
:root{
  --green:#8cc63e;
  --green-dark:#6fa82a;
  --green-pale:#dcedc4;
  --ink:#222;
  --grey:#555;
  --row-alt:#f3f3f3;
  --line:#c9c9c9;
  --white:#fff;
}
*{box-sizing:border-box;margin:0;padding:0}
html,body{width:849px;height:1200px;overflow:hidden;background:var(--white)}
body{position:relative;font-family:"Open Sans",Arial,sans-serif;color:var(--ink)}
.brand{position:absolute;left:22px;top:14px;display:flex;align-items:center;gap:7px}
.brand-dot{width:14px;height:14px;border-radius:50%;background:var(--green)}
.brand-name{font-family:"Montserrat",Arial,sans-serif;font-weight:800;font-size:22px;letter-spacing:1px;color:#3a3a3a}
.corner-bands{position:absolute;right:0;top:0}
.title-band{position:absolute;left:37px;top:60px;width:775px;height:34px;background:var(--green);
  clip-path:polygon(14px 0,100% 0,calc(100% - 14px) 100%,0 100%);
  display:flex;align-items:center;justify-content:center}
.title-band h1{font-family:"Montserrat",Arial,sans-serif;font-weight:700;font-size:23px;color:var(--white);letter-spacing:1.5px}
.matrix{position:absolute;left:37px;top:95px;width:775px;border-collapse:collapse;table-layout:fixed;font-size:8.5px}
.matrix col.dish{width:148px}
.matrix th,.matrix td{border:1px solid var(--line)}
.matrix thead th{height:98px;vertical-align:bottom;padding:3px 0 4px}
.matrix .dish-head{font-family:"Montserrat",Arial,sans-serif;font-size:13px;font-weight:700;text-align:center;vertical-align:middle}
.allergen{display:flex;flex-direction:column;align-items:center;gap:4px}
.allergen span{writing-mode:vertical-rl;transform:rotate(180deg);font-weight:700;font-size:9px;line-height:1.05;text-align:left;max-height:70px}
.allergen i{width:16px;height:16px;border:1.5px solid var(--green);border-radius:50%;display:block}
.section td{background:var(--green-pale);font-family:"Montserrat",Arial,sans-serif;font-weight:700;font-size:10.5px;text-align:center;height:15px}
.matrix tbody tr.item td{height:24px}
.matrix tbody tr.item.two td{height:36px}
.matrix tbody.salads tr.item td{height:19px}
.matrix tbody tr.item:nth-child(odd) td{background:var(--row-alt)}
.matrix td.dish{padding:1px 5px;font-weight:600;line-height:1.25}
.matrix td.mark{text-align:center;font-size:11px;font-weight:700}
.may{color:var(--grey);font-weight:400}
.revisions{position:absolute;left:37px;top:760px;width:775px;border-collapse:collapse;font-size:8.5px}
.revisions th{background:var(--green);color:var(--white);font-weight:700;height:17px;border:1px solid var(--white)}
.revisions td{height:15px;border:1px solid var(--line);padding:0 6px}
.revisions td:first-child,.revisions td:nth-child(2){text-align:center}
.revisions col.no{width:120px}
.revisions col.date{width:120px}
.note{position:absolute;left:37px;top:840px;width:775px;font-size:8px;color:var(--ink);line-height:1.35}
.note .lead{color:#c0392b;font-weight:600}
.contact-bar{position:absolute;left:37px;top:1132px;width:775px;height:26px;background:var(--green);border-radius:13px;
  display:flex;align-items:center;justify-content:space-around;color:var(--white);font-size:10px;font-weight:600}
.contact-bar span{display:flex;align-items:center;gap:5px}
.website{position:absolute;left:0;top:1166px;width:849px;text-align:center;font-family:"Montserrat",Arial,sans-serif;font-weight:700;font-size:13px;color:var(--ink)}
</style>
</head>
<body>
<header class="brand">
  <span class="brand-dot"></span><span class="brand-name">KESTRAN</span>
</header>
<svg class="corner-bands" width="260" height="58" viewBox="0 0 260 58">
  <polygon points="60,0 120,0 90,58 30,58" fill="#8cc63e"/>
  <polygon points="130,0 170,0 140,58 100,58" fill="#a9d46a"/>
  <polygon points="180,0 260,0 260,58 150,58" fill="#8cc63e"/>
</svg>

<div class="title-band"><h1>ALLERGEN MATRIX</h1></div>

<table class="matrix">
  <colgroup><col class="dish"><col span="14"></colgroup>
  <thead>
    <tr>
      <th class="dish-head">DISHES</th>
      <th><div class="allergen"><span>Celery</span><i></i></div></th>
      <th><div class="allergen"><span>Cereals containing gluten</span><i></i></div></th>
      <th><div class="allergen"><span>Crustaceans</span><i></i></div></th>
      <th><div class="allergen"><span>Eggs</span><i></i></div></th>
      <th><div class="allergen"><span>Fish</span><i></i></div></th>
      <th><div class="allergen"><span>Lupin</span><i></i></div></th>
      <th><div class="allergen"><span>Milk</span><i></i></div></th>
      <th><div class="allergen"><span>Molluscs</span><i></i></div></th>
      <th><div class="allergen"><span>Mustard</span><i></i></div></th>
      <th><div class="allergen"><span>Nuts</span><i></i></div></th>
      <th><div class="allergen"><span>Peanuts</span><i></i></div></th>
      <th><div class="allergen"><span>Sesame seeds</span><i></i></div></th>
      <th><div class="allergen"><span>Soya</span><i></i></div></th>
      <th><div class="allergen"><span>Sulphur dioxide</span><i></i></div></th>
    </tr>
  </thead>
  <tbody class="sandwiches">
    <tr class="section"><td colspan="15">Sandwiches &amp; Wraps</td></tr>
    <tr class="item"><td class="dish">Chicken Bacon Wrap</td><td class="mark">✔</td><td class="mark">✔</td><td class="mark"></td><td class="mark">✔</td><td class="mark"></td><td class="mark"></td><td class="mark"></td><td class="mark"></td><td class="mark">✔</td><td class="mark"></td><td class="mark"></td><td class="mark"></td><td class="mark"></td><td class="mark"></td></tr>
    <tr class="item two"><td class="dish">Cream Cheese, Salmon &amp; Bagel</td><td class="mark"></td><td class="mark">✔</td><td class="mark"></td><td class="mark"></td><td class="mark">✔</td><td class="mark"></td><td class="mark">✔</td><td class="mark"></td><td class="mark"></td><td class="mark"></td><td class="mark"></td><td class="mark"></td><td class="mark"></td><td class="mark"></td></tr>
    <tr class="item two"><td class="dish">Roasted Veggies, Mayo Sauce, Ciabatta</td><td class="mark">✔</td><td class="mark">✔</td><td class="mark"></td><td class="mark">✔</td><td class="mark"></td><td class="mark"></td><td class="mark">✔</td><td class="mark"></td><td class="mark">✔</td><td class="mark"></td><td class="mark"></td><td class="mark"></td><td class="mark"></td><td class="mark"></td></tr>
    <tr class="item two"><td class="dish">Chicken Sandwich, Mayo Sauce, Walnut, Potato Bun</td><td class="mark">✔</td><td class="mark">✔</td><td class="mark"></td><td class="mark">✔</td><td class="mark"></td><td class="mark"></td><td class="mark">✔</td><td class="mark"></td><td class="mark">✔</td><td class="mark">✔</td><td class="mark"></td><td class="mark"></td><td class="mark"></td><td class="mark may">○</td></tr>
    <tr class="item"><td class="dish">Grilled Cheese Sandwich</td><td class="mark"></td><td class="mark">✔</td><td class="mark"></td><td class="mark"></td><td class="mark"></td><td class="mark"></td><td class="mark">✔</td><td class="mark"></td><td class="mark"></td><td class="mark"></td><td class="mark"></td><td class="mark"></td><td class="mark"></td><td class="mark"></td></tr>
    <tr class="item two"><td class="dish">Avocado on Toast with Cheese Spread</td><td class="mark"></td><td class="mark">✔</td><td class="mark"></td><td class="mark"></td><td class="mark"></td><td class="mark"></td><td class="mark">✔</td><td class="mark"></td><td class="mark"></td><td class="mark"></td><td class="mark"></td><td class="mark"></td><td class="mark"></td><td class="mark"></td></tr>
    <tr class="item"><td class="dish">Spinach &amp; Tahini Pastry Roll</td><td class="mark"></td><td class="mark">✔</td><td class="mark"></td><td class="mark">✔</td><td class="mark"></td><td class="mark"></td><td class="mark">✔</td><td class="mark"></td><td class="mark"></td><td class="mark"></td><td class="mark"></td><td class="mark">✔</td><td class="mark"></td><td class="mark"></td></tr>
    <tr class="item"><td class="dish">Feta Cheese Pastry Roll</td><td class="mark"></td><td class="mark">✔</td><td class="mark"></td><td class="mark">✔</td><td class="mark"></td><td class="mark"></td><td class="mark">✔</td><td class="mark"></td><td class="mark"></td><td class="mark"></td><td class="mark"></td><td class="mark"></td><td class="mark"></td><td class="mark"></td></tr>
    <tr class="item"><td class="dish">Feta Cheese &amp; Honey Pastry</td><td class="mark"></td><td class="mark">✔</td><td class="mark"></td><td class="mark">✔</td><td class="mark"></td><td class="mark"></td><td class="mark">✔</td><td class="mark"></td><td class="mark"></td><td class="mark"></td><td class="mark"></td><td class="mark">✔</td><td class="mark"></td><td class="mark"></td></tr>
    <tr class="item"><td class="dish">Chicken, Mayo, Mustard Wrap</td><td class="mark">✔</td><td class="mark">✔</td><td class="mark"></td><td class="mark">✔</td><td class="mark"></td><td class="mark"></td><td class="mark"></td><td class="mark"></td><td class="mark">✔</td><td class="mark"></td><td class="mark"></td><td class="mark"></td><td class="mark"></td><td class="mark may">○</td></tr>
    <tr class="item"><td class="dish">Falafel, Hummus Wrap</td><td class="mark">✔</td><td class="mark">✔</td><td class="mark"></td><td class="mark">✔</td><td class="mark"></td><td class="mark"></td><td class="mark"></td><td class="mark"></td><td class="mark"></td><td class="mark"></td><td class="mark"></td><td class="mark"></td><td class="mark"></td><td class="mark"></td></tr>
  </tbody>
  <tbody class="salads">
    <tr class="section"><td colspan="15">Salads &amp; Hot Lunch Meals</td></tr>
    <tr class="item"><td class="dish">Bulgur Salad</td><td class="mark">✔</td><td class="mark">✔</td><td class="mark"></td><td class="mark"></td><td class="mark"></td><td class="mark"></td><td class="mark"></td><td class="mark"></td><td class="mark"></td><td class="mark"></td><td class="mark"></td><td class="mark"></td><td class="mark"></td><td class="mark"></td></tr>
    <tr class="item"><td class="dish">Mung Bean Salad</td><td class="mark">✔</td><td class="mark"></td><td class="mark"></td><td class="mark"></td><td class="mark"></td><td class="mark"></td><td class="mark"></td><td class="mark"></td><td class="mark"></td><td class="mark"></td><td class="mark"></td><td class="mark"></td><td class="mark"></td><td class="mark"></td></tr>
    <tr class="item"><td class="dish">Black-eyed Beans Salad</td><td class="mark">✔</td><td class="mark"></td><td class="mark"></td><td class="mark"></td><td class="mark"></td><td class="mark"></td><td class="mark"></td><td class="mark"></td><td class="mark"></td><td class="mark"></td><td class="mark"></td><td class="mark"></td><td class="mark"></td><td class="mark">✔</td></tr>
    <tr class="item"><td class="dish">Chickpea Salad</td><td class="mark">✔</td><td class="mark"></td><td class="mark"></td><td class="mark"></td><td class="mark"></td><td class="mark"></td><td class="mark"></td><td class="mark"></td><td class="mark"></td><td class="mark"></td><td class="mark"></td><td class="mark"></td><td class="mark"></td><td class="mark"></td></tr>
    <tr class="item"><td class="dish">Peas Salad</td><td class="mark">✔</td><td class="mark"></td><td class="mark"></td><td class="mark"></td><td class="mark"></td><td class="mark"></td><td class="mark"></td><td class="mark"></td><td class="mark"></td><td class="mark"></td><td class="mark"></td><td class="mark"></td><td class="mark"></td><td class="mark"></td></tr>
    <tr class="item"><td class="dish">Carrot Salad</td><td class="mark">✔</td><td class="mark"></td><td class="mark"></td><td class="mark"></td><td class="mark"></td><td class="mark"></td><td class="mark"></td><td class="mark"></td><td class="mark"></td><td class="mark"></td><td class="mark"></td><td class="mark"></td><td class="mark"></td><td class="mark"></td></tr>
    <tr class="item"><td class="dish">Celeriac Salad</td><td class="mark">✔</td><td class="mark"></td><td class="mark"></td><td class="mark">✔</td><td class="mark"></td><td class="mark"></td><td class="mark">✔</td><td class="mark"></td><td class="mark"></td><td class="mark"></td><td class="mark"></td><td class="mark"></td><td class="mark"></td><td class="mark"></td></tr>
    <tr class="item"><td class="dish">Beetroot Salad</td><td class="mark">✔</td><td class="mark"></td><td class="mark"></td><td class="mark"></td><td class="mark"></td><td class="mark"></td><td class="mark"></td><td class="mark"></td><td class="mark"></td><td class="mark"></td><td class="mark"></td><td class="mark">✔</td><td class="mark"></td><td class="mark"></td></tr>
    <tr class="item"><td class="dish">Shakshuka</td><td class="mark">✔</td><td class="mark">✔</td><td class="mark"></td><td class="mark">✔</td><td class="mark"></td><td class="mark"></td><td class="mark"></td><td class="mark"></td><td class="mark"></td><td class="mark"></td><td class="mark"></td><td class="mark"></td><td class="mark"></td><td class="mark"></td></tr>
    <tr class="item"><td class="dish">Ham&amp;Cheese Croissant</td><td class="mark may">○</td><td class="mark">✔</td><td class="mark"></td><td class="mark">✔</td><td class="mark may">○</td><td class="mark"></td><td class="mark">✔</td><td class="mark may">○</td><td class="mark may">○</td><td class="mark may">○</td><td class="mark may">○</td><td class="mark may">○</td><td class="mark may">○</td><td class="mark may">○</td></tr>
    <tr class="item"><td class="dish">Porridge with Oatmilk</td><td class="mark"></td><td class="mark">✔</td><td class="mark"></td><td class="mark"></td><td class="mark"></td><td class="mark"></td><td class="mark"></td><td class="mark"></td><td class="mark"></td><td class="mark"></td><td class="mark may">○</td><td class="mark"></td><td class="mark"></td><td class="mark"></td></tr>
  </tbody>
</table>

<table class="revisions">
  <colgroup><col class="no"><col class="date"><col></colgroup>
  <thead><tr><th>Revision No</th><th>Revision Date</th><th>Explanation</th></tr></thead>
  <tbody>
    <tr><td>00</td><td>13.10.2023</td><td>Preparation</td></tr>
    <tr><td>01</td><td>14.10.2024</td><td>Butter beans salad has been added</td></tr>
    <tr><td>03</td><td>18.10.2024</td><td>Removed this dish</td></tr>
  </tbody>
</table>

<p class="note"><span class="lead">All above are shared for general guidance purposes. The Allergen list should be revised regularly.</span><br>
KESTRAN Works Limited does not accept responsibility for potential allergen reactions.<br>
"O" (May Contain), (Contains), (Removable), (GMO) (Colorant)</p>

<footer class="contact-bar">
  <span><svg width="11" height="13" viewBox="0 0 11 13"><path d="M5.5 0C2.5 0 0 2.4 0 5.3 0 9 5.5 13 5.5 13S11 9 11 5.3C11 2.4 8.5 0 5.5 0zm0 7.3a2 2 0 110-4 2 2 0 010 4z" fill="#fff"/></svg>12 Harlow Street, NW3 4TQ, London UK</span>
  <span><svg width="12" height="12" viewBox="0 0 12 12"><path d="M2.4 0.5l2 2.3-1 1.5c.8 1.6 2 2.8 3.6 3.6l1.5-1 2.3 2-1.2 2.1C5 10.8 1.2 7 .3 2.4z" fill="#fff"/></svg>+44 (0)330 000 412</span>
  <span><svg width="13" height="10" viewBox="0 0 13 10"><rect x="0.5" y="0.5" width="12" height="9" rx="1" fill="none" stroke="#fff"/><path d="M0.5 1l6 4.5 6-4.5" fill="none" stroke="#fff"/></svg>info@kestranworks.co.uk</span>
</footer>
<div class="website">www.kestranworks.co.uk</div>
</body>
</html>
```